its a new company based in Christchurch new Zealand building computers ,repairs, upgrades and anything computers for the general public,i like bright happy colours like yellows, greens reds anything that stands out and it needs to communicant trust and security towards my new company,i have no logo yet,

Target Market(s)

target market of all ages

Industry/Entity Type

Building

Contact Information for Business Card

Pixel Harbour Limited,ph-0274829315,email-brightnode47@mailvista.example,14c tamworth cl,kelvale

```html
<!DOCTYPE html>
<html lang="en">
<head>
<meta charset="utf-8">
<title>Pixel Harbour Limited — Business Card</title>
<link rel="stylesheet" href="https://fonts.googleapis.com/css2?family=Saira:wght@400;600&display=swap">
<style>
  :root {
    --backdrop: #2b2b2d;
    --card: #f7f7f6;
    --brand-blue: #2a78c2;
    --brand-orange: #f39a1c;
    --ink: #2a2a2a;
    --rule: #b9c9da;
  }
  * { box-sizing: border-box; margin: 0; padding: 0; }
  html, body {
    width: 1200px;
    height: 900px;
    overflow: hidden;
    background: var(--backdrop);
    font-family: "Saira", sans-serif;
  }
  .stage {
    width: 1200px;
    height: 900px;
    display: flex;
    align-items: center;
    justify-content: center;
    gap: 40px;
  }
  .card {
    position: relative;
    width: 525px;
    height: 300px;
    background: var(--card);
    border-radius: 3px;
    box-shadow: 0 14px 30px rgba(0,0,0,0.45);
  }

  /* Front side */
  .card-front .wordmark {
    position: absolute;
    top: 100px;
    left: 0;
    right: 0;
    display: flex;
    align-items: center;
    justify-content: center;
    gap: 12px;
    color: var(--brand-blue);
    font-size: 34px;
    font-weight: 600;
  }
  .wordmark-square {
    width: 22px;
    height: 22px;
    background: var(--brand-orange);
  }
  .card-front .tagline {
    position: absolute;
    left: 60px;
    bottom: 46px;
    font-size: 13px;
    color: var(--ink);
  }

  /* Back side */
  .card-back .details {
    position: absolute;
    top: 40px;
    left: 150px;
    width: 300px;
    text-align: center;
  }
  .company-name {
    color: var(--brand-blue);
    font-size: 19px;
    font-weight: 600;
    margin-bottom: 6px;
  }
  .field-label {
    display: block;
    color: var(--brand-orange);
    font-size: 8px;
    letter-spacing: 0.06em;
    text-transform: uppercase;
    line-height: 1;
  }
  .field-value {
    display: block;
    color: var(--brand-blue);
    line-height: 1.2;
  }
  .phone .field-value { font-size: 19px; }
  .email .field-value { font-size: 13px; }
  .rule {
    height: 1px;
    background: var(--rule);
    margin: 6px 0 5px;
  }
  .address {
    color: var(--brand-orange);
    font-size: 13px;
  }
  .card-back .wordmark {
    margin-top: 16px;
    display: flex;
    align-items: center;
    justify-content: center;
    gap: 7px;
    color: var(--brand-blue);
    font-size: 17px;
    font-weight: 600;
  }
  .card-back .wordmark-square { width: 12px; height: 12px; }
</style>
</head>
<body>
  <main class="stage">
    <section class="card card-front" aria-label="Business card front">
      <div class="wordmark">
        <span class="wordmark-square" aria-hidden="true"></span>
        <span>Pixel Harbour Limited</span>
      </div>
      <p class="tagline">building computers, repairs, upgrades, anything computers.....</p>
    </section>

    <section class="card card-back" aria-label="Business card back">
      <div class="details">
        <h1 class="company-name">Pixel Harbour Limited</h1>
        <p class="phone">
          <span class="field-label">Phone</span>
          <span class="field-value">0274829315</span>
        </p>
        <p class="email">
          <span class="field-label">Email</span>
          <span class="field-value">brightnode47@mailvista.example</span>
        </p>
        <div class="rule"></div>
        <p class="address">14C Tamworth Cl, Kelvale</p>
        <div class="rule"></div>
        <div class="wordmark">
          <span class="wordmark-square" aria-hidden="true"></span>
          <span>Pixel Harbour Limited</span>
        </div>
      </div>
    </section>
  </main>
</body>
</html>
```